Kindle Grove Wording For Logo & Business card

I have the logo, I just need the "kindle Grove" wording to go with it, and a business card design. The only thing on the business card is the website info. We provide nature connection experiences, and bolster these efforts through writing and host a platform for community around it.

I also have an idea of what it could look like (sketch), though I'm really not sure how it would come out. I am open to the best design and happy to consider original artwork. You can see what the site is about at KindleGrove.com.

Contact Information for Business Card

The only thing on the business card is the website info and the design. I will put other messaging on the back.

Website lettering (KindleGrove.com) in Montserrat

Logo Text

Kindle Grove (letters optional)

Font styles to use
Other font styles liked:
• montserrat

```html
<!DOCTYPE html>
<html lang="en">
<head>
<meta charset="utf-8">
<title>Kindle Grove – Business Card</title>
<link rel="stylesheet" href="https://fonts.googleapis.com/css2?family=Jost:wght@400;600&family=Montserrat:wght@300;400&display=swap">
<style>
  :root {
    --page-bg: #3a3a3c;
    --card-bg: #ffffff;
    --ink: #1d1530;
    --ember: #f7941d;
    --emblem-core: #1a1030;
    --emblem-mid: #2b1a45;
    --emblem-edge: #e8561c;
  }
  * { margin: 0; padding: 0; box-sizing: border-box; }
  html, body { width: 1200px; height: 583px; overflow: hidden; }
  body { background: var(--page-bg); position: relative; font-family: "Montserrat", sans-serif; }

  .card {
    position: absolute;
    top: 154px;
    width: 481px;
    height: 275px;
    background: var(--card-bg);
    border-radius: 38px;
    overflow: hidden;
  }
  .card--front { left: 94px; }
  .card--back { left: 627px; }

  .emblem-art { position: absolute; display: block; }
  .card--front .emblem-art { left: -50px; top: 50px; width: 254px; height: 254px; }
  .card--back .emblem-art { left: 275px; top: 68px; width: 260px; height: 260px; }

  .brand {
    position: absolute;
    left: 228px;
    top: 112px;
    display: flex;
    align-items: center;
    gap: 7px;
  }
  .brand__dot {
    width: 54px; height: 54px;
    border-radius: 50%;
    background: var(--emblem-core);
    flex: none;
  }
  .brand__text { display: flex; flex-direction: column; }
  .brand__name {
    font-weight: 300;
    font-size: 22px;
    letter-spacing: 1.5px;
    color: var(--ink);
    line-height: 1;
  }
  .brand__web {
    margin-top: 5px;
    font-size: 8px;
    letter-spacing: 3.6px;
    color: var(--ink);
  }
  .brand__web span { color: var(--ember); }

  .contact { position: absolute; left: 44px; top: 72px; font-family: "Jost", sans-serif; }
  .contact__name { font-weight: 600; font-size: 31px; color: var(--ink); line-height: 1; letter-spacing: -0.5px; }
  .contact__role { font-size: 17px; color: var(--ember); margin-top: 4px; }
  .contact__list { list-style: none; margin-top: 19px; }
  .contact__item {
    display: flex; align-items: center; gap: 6px;
    font-size: 13px; color: var(--ember); height: 19px;
  }
  .contact__icon { width: 11px; height: 11px; flex: none; }
</style>
</head>
<body>
  <section class="card card--front">
    <svg class="emblem-art" viewBox="0 0 100 100" role="img" aria-label="Large flame emblem in orange and deep purple">
      <defs>
        <radialGradient id="emblemGlowFront">
          <stop offset="0" stop-color="var(--emblem-mid)"/>
          <stop offset="0.78" stop-color="var(--emblem-core)"/>
          <stop offset="1" stop-color="var(--emblem-edge)"/>
        </radialGradient>
      </defs>
      <circle cx="50" cy="50" r="50" fill="url(#emblemGlowFront)"/>
    </svg>
    <div class="brand">
      <span class="brand__dot"></span>
      <div class="brand__text">
        <span class="brand__name">KINDLE GROVE</span>
        <span class="brand__web">www.<span>kindlegrove</span>.com</span>
      </div>
    </div>
  </section>

  <section class="card card--back">
    <div class="contact">
      <h1 class="contact__name">MARA ELLWOOD</h1>
      <p class="contact__role">Manager</p>
      <ul class="contact__list">
        <li class="contact__item">
          <svg class="contact__icon" viewBox="0 0 12 12"><circle cx="6" cy="6" r="6" fill="var(--ink)"/><path d="M4 3.2l1 .1.5 1.5-.7.6a4 4 0 0 0 1.8 1.8l.6-.7 1.5.5.1 1a1 1 0 0 1-1 .8A5 5 0 0 1 3.2 4.2a1 1 0 0 1 .8-1z" fill="#fff"/></svg>
          555-204-7781
        </li>
        <li class="contact__item">
          <svg class="contact__icon" viewBox="0 0 12 12"><circle cx="6" cy="6" r="6" fill="var(--ink)"/><rect x="3" y="4" width="6" height="4.2" fill="#fff"/><path d="M3 4l3 2.3L9 4" stroke="var(--ink)" stroke-width=".7" fill="none"/></svg>
          hello@kindlegrove.com
        </li>
        <li class="contact__item">
          <svg class="contact__icon" viewBox="0 0 12 12"><circle cx="6" cy="6" r="6" fill="var(--ink)"/><path d="M6 2.8L9 5.4V9H7V7H5v2H3V5.4z" fill="#fff"/></svg>
          14 Cedar Lane, Ashford, box 40217
        </li>
      </ul>
    </div>
    <svg class="emblem-art" viewBox="0 0 100 100" role="img" aria-label="Large flame emblem in orange and deep purple">
      <defs>
        <radialGradient id="emblemGlowBack">
          <stop offset="0" stop-color="var(--emblem-mid)"/>
          <stop offset="0.78" stop-color="var(--emblem-core)"/>
          <stop offset="1" stop-color="var(--emblem-edge)"/>
        </radialGradient>
      </defs>
      <circle cx="50" cy="50" r="50" fill="url(#emblemGlowBack)"/>
    </svg>
  </section>
</body>
</html>
```